Business card design needed

Name of Restaurant:
Willow Crossing
The Restaurant with a Difference

Target Market(s)

Food lovers, families

Industry/Entity Type

Business

Contact Information for Business Card

Mountains, sun rays

Logo Text

Willow Crossing The Restaurant with a difference

Logo styles of interest
Pictorial/Combination Logo
Abstract Logo
Requirements
Must have
• Mountains
Nice to have
• Sun rays

```html
<!DOCTYPE html>
<html lang="en">
<head>
<meta charset="utf-8">
<title>Willow Crossing – Business Card</title>
<link href="https://fonts.googleapis.com/css2?family=Open+Sans:wght@300;700&family=Roboto:wght@300;400;700&display=swap" rel="stylesheet">
<style>
  :root {
    --board: #1c1c1c;
    --label: #5a5a5a;
    --red: #ed1c24;
    --red-dark: #be1e2d;
    --grey-70: #6d6e71;
    --grey-30: #c7c8ca;
    --band: #bcbdbf;
    --text: #6a6a6a;
    --white: #ffffff;
  }
  * { margin: 0; padding: 0; box-sizing: border-box; }
  html, body { width: 1200px; height: 1000px; overflow: hidden; background: var(--board); }
  .board { position: relative; width: 1200px; height: 1000px; background: var(--board); font-family: "Roboto", Arial, sans-serif; }

  .side-label { position: absolute; font-family: "Open Sans", Arial, sans-serif; font-weight: 300; font-size: 30px; color: var(--label); }
  .side-label.front { left: 174px; top: 282px; }
  .side-label.back { left: 174px; top: 677px; }
  .side-label.size { left: 931px; top: 282px; }

  .card { position: absolute; left: 343px; width: 514px; height: 285px; box-shadow: 0 18px 30px rgba(0,0,0,.55); }
  .card-front { top: 160px; background: var(--white); }
  .card-back { top: 554px; background: var(--red); }

  .front-divider { position: absolute; left: 171px; top: 0; width: 1px; height: 285px; background: #c8c8c8; }
  .brand { position: absolute; text-align: center; font-weight: 400; line-height: 1; }
  .brand-mark { display: block; margin: 0 auto 12px; width: 22px; height: 22px; }
  .card-front .brand { left: 0; width: 171px; top: 62px; color: var(--red); font-size: 28px; }
  .card-front .brand-mark { background: var(--red); }
  .card-back .brand { left: 0; width: 514px; top: 62px; color: var(--white); font-size: 34px; }
  .card-back .brand-mark { background: var(--white); width: 30px; height: 30px; }

  .name-band { position: absolute; left: 172px; top: 64px; width: 342px; height: 56px; background: var(--band); color: var(--white); padding: 4px 0 0 27px; }
  .person-name { font-size: 24px; font-weight: 300; line-height: 30px; }
  .person-title { font-size: 12px; font-weight: 700; letter-spacing: .2px; line-height: 14px; }

  .contact-list { position: absolute; left: 198px; top: 134px; list-style: none; font-size: 14px; color: var(--text); }
  .contact-list li { position: relative; height: 22.3px; line-height: 22px; padding-left: 28px; }
  .contact-list svg { position: absolute; left: 0; top: 5px; width: 14px; height: 14px; fill: var(--red); }

  .tagline { position: absolute; left: 0; width: 514px; top: 233px; text-align: center; color: var(--white); font-size: 9.5px; font-weight: 700; letter-spacing: .2px; }

  .swatch { position: absolute; top: 814px; width: 26px; height: 26px; }
  .swatch-code { position: absolute; bottom: 200px; writing-mode: vertical-rl; transform: rotate(180deg); font-family: "Open Sans", Arial, sans-serif; font-weight: 700; font-size: 16px; letter-spacing: 1.5px; color: var(--label); white-space: nowrap; }
</style>
</head>
<body>
<div class="board">
  <span class="side-label front">front</span>
  <span class="side-label back">back</span>
  <span class="side-label size">90 x 50 mm</span>

  <section class="card card-front">
    <div class="brand"><span class="brand-mark"></span>Willow<br>Crossing</div>
    <div class="front-divider"></div>
    <div class="name-band">
      <div class="person-name">Marlene Oberholt</div>
      <div class="person-title">YOUR TITLE HERE</div>
    </div>
    <ul class="contact-list">
      <li><svg viewBox="0 0 14 14"><path d="M5 0h4v5h5v4H9v5H5V9H0V5h5z"/></svg>Lorem ipsum dolor sit amet 18B, Swiss</li>
      <li><svg viewBox="0 0 14 14"><path d="M3 0l3 3-1.5 2c1 2 2.5 3.5 4.5 4.5L11 8l3 3-2 2C6 13 1 8 1 2z"/></svg>+41 55 210 3847</li>
      <li>+41 55 210 3847</li>
      <li><svg viewBox="0 0 14 14"><path d="M0 2h14v1L7 8 0 3zM0 5l7 5 7-5v7H0z"/></svg>marlene@willowcrossing.com</li>
      <li><svg viewBox="0 0 14 14" fill="none"><g fill="none" stroke="#ed1c24" stroke-width="1.3"><circle cx="7" cy="7" r="6"/><ellipse cx="7" cy="7" rx="2.6" ry="6"/><path d="M1 7h12M2 3.8h10M2 10.2h10"/></g></svg>www.willowcrossing.com</li>
    </ul>
  </section>

  <section class="card card-back">
    <div class="brand"><span class="brand-mark"></span>Willow<br>Crossing</div>
    <div class="tagline">THE RESTAURANT WITH A DIFFERENCE</div>
  </section>

  <div class="swatch" style="left:931px;background:var(--red)"></div>
  <div class="swatch" style="left:983px;background:var(--red-dark)"></div>
  <div class="swatch" style="left:1033px;background:var(--grey-70)"></div>
  <div class="swatch" style="left:1084px;background:var(--grey-30)"></div>
  <span class="swatch-code" style="left:933px">C0 M100 Y100 K0</span>
  <span class="swatch-code" style="left:985px">C15 M100 Y90 K15</span>
  <span class="swatch-code" style="left:1035px">BLACK 70%</span>
  <span class="swatch-code" style="left:1086px">BLACK 30%</span>
</div>
</body>
</html>
```